Joan Pelley Letter Head

log and letter head

would like a modern feminine approch, please see attached the back of my business card

Joan Pelley Consulting

ABN 81 305 642 918

Address19a Brood Street Semaphore South 5019 South Australia

Business

```html
<!DOCTYPE html>
<html lang="en">
<head>
<meta charset="utf-8">
<title>Joan Pelley Consulting – Letterhead</title>
<link href="https://fonts.googleapis.com/css2?family=Dosis:wght@300;400&display=swap" rel="stylesheet">
<style>
  :root {
    --page-pink: #fde6fd;
    --sheet-white: #ffffff;
    --art-pink: #f2b3fb;
    --art-soft: #f7cffc;
    --ink-violet: #8a1cf0;
  }
  html, body {
    margin: 0;
    padding: 0;
    overflow: hidden;
    background: var(--page-pink);
  }
  .letterhead {
    position: relative;
    width: 848px;
    height: 1200px;
    overflow: hidden;
    background: var(--page-pink);
    font-family: "Dosis", sans-serif;
  }
  .writing-area {
    position: absolute;
    left: 60px;
    top: 200px;
    width: 760px;
    height: 900px;
    border-radius: 48px;
    background: var(--sheet-white);
  }
  .decor-artwork {
    position: absolute;
    left: 0;
    top: 430px;
    width: 540px;
    height: 770px;
    background: linear-gradient(160deg, var(--art-pink) 0%, var(--art-soft) 55%, var(--page-pink) 100%);
    opacity: 0.85;
  }
  .sender {
    position: absolute;
    top: 50px;
    right: 48px;
    text-align: right;
    color: var(--ink-violet);
  }
  .sender-name {
    margin: 0 0 28px;
    font-size: 34px;
    font-weight: 300;
    line-height: 1.1;
  }
  .sender-detail {
    margin: 0 0 11px;
    font-size: 15px;
    font-weight: 400;
    line-height: 1.2;
  }
</style>
</head>
<body>
  <div class="letterhead">
    <div class="writing-area"></div>
    <div class="decor-artwork" role="img" aria-label="Decorative pink geometric artwork"></div>

    <header class="sender">
      <h1 class="sender-name">Joan Pelley Consulting</h1>
      <p class="sender-detail">ABN 81 305 642 918</p>
      <p class="sender-detail">Address47c Tallow Street Semaphore South 5019 South Australia</p>
    </header>
  </div>
</body>
</html>
```